Design a building access mobile app for Wopel by Quillstone Access Controls

Hello, We're looking for an awesome designer to create an app design for our app Wopel, by Quillstone Access Controls. the mobile app allows employees open their office doors with their mobile phone. this means they don't have to use those plastic card badges or keys. We like clean modern design, dark and light themes. We don't have a logo yet.

Target Market(s)

Commercial and employees

Industry/Entity Type

Building

Font styles to use
Sans Serif
Other font styles liked:
• Oswald extra light

Requirements
Must have
• nice clean design

```html
<!DOCTYPE html>
<html lang="en">
<head>
<meta charset="utf-8">
<title>Wopel – Sign Up</title>
<link rel="stylesheet" href="https://fonts.googleapis.com/css2?family=Oswald:wght@200;300;400;500;600&family=Roboto:wght@500&display=swap">
<style>
  :root {
    --brand-red: #b11d32;
    --brand-red-deep: #a3172b;
    --brand-red-light: #bd2a3e;
    --field-fill: rgba(255, 255, 255, 0.2);
    --field-shadow: rgba(90, 0, 15, 0.35);
    --text-white: #ffffff;
    --text-muted: rgba(255, 255, 255, 0.62);
    --placeholder: rgba(255, 255, 255, 0.55);
    --accent-green: #7ed321;
    --button-green: #4c9a1e;
  }
  * { box-sizing: border-box; margin: 0; padding: 0; }
  html, body {
    width: 675px; height: 1200px; overflow: hidden;
    background: var(--brand-red);
  }
  .screen {
    position: relative; width: 675px; height: 1200px; overflow: hidden;
    font-family: "Oswald", sans-serif; color: var(--text-white);
  }
  .backdrop {
    position: absolute; inset: 0;
    background:
      radial-gradient(ellipse at 70% 40%, var(--brand-red-light) 0%, transparent 60%),
      linear-gradient(160deg, var(--brand-red) 0%, var(--brand-red-deep) 100%);
  }
  .status-bar {
    position: absolute; top: 0; left: 0; right: 0; height: 40px;
    font-family: "Roboto", sans-serif; font-weight: 500; font-size: 14px;
  }
  .status-bar .signal { position: absolute; left: 10px; top: 13px; }
  .status-bar .time { position: absolute; left: 0; right: 0; top: 11px; text-align: center; }
  .status-bar .power { position: absolute; right: 10px; top: 11px; display: flex; align-items: center; gap: 4px; }
  .brand-name {
    position: absolute; top: 338px; left: 0; right: 0; text-align: center;
    font-weight: 400; font-size: 46px; line-height: 1.2; letter-spacing: 0.2px;
  }
  .page-title {
    position: absolute; top: 460px; left: 0; right: 0; text-align: center;
    font-weight: 300; font-size: 38px; line-height: 1.2;
  }
  .page-title span { border-bottom: 1px solid var(--text-white); padding-bottom: 1px; }
  .field {
    position: absolute; left: 50px; width: 575px; height: 72px;
    background: var(--field-fill); border-radius: 4px;
    box-shadow: 0 2px 2px var(--field-shadow);
    display: flex; align-items: center; padding: 0 22px 0 23px;
  }
  .field .value, .field .placeholder { flex: 1; font-weight: 300; font-size: 32px; line-height: 1; }
  .field .placeholder { color: var(--placeholder); }
  .field .caret { display: inline-block; width: 1px; height: 44px; background: var(--text-white); vertical-align: middle; margin-left: 4px; }
  .field svg { flex: none; }
  .field-email { top: 593px; }
  .field-password { top: 686px; }
  .field-confirm { top: 778px; }
  .touch-option {
    position: absolute; left: 53px; top: 886px; display: flex; align-items: center; gap: 18px;
    font-weight: 300; font-size: 33px;
  }
  .checkbox { width: 32px; height: 32px; border: 2px solid var(--accent-green); border-radius: 3px; display: flex; align-items: center; justify-content: center; }
  .register-button {
    position: absolute; left: 50px; top: 978px; width: 575px; height: 72px;
    background: var(--button-green); border-radius: 4px;
    box-shadow: 0 2px 2px var(--field-shadow);
    display: flex; align-items: center; justify-content: center;
    font-weight: 600; font-size: 34px; color: var(--text-white);
  }
  .login-prompt {
    position: absolute; top: 1114px; left: 0; right: 0; text-align: center;
    font-weight: 200; font-size: 31px; color: var(--text-muted);
  }
  .login-prompt .login-link { color: var(--accent-green); font-weight: 300; font-size: 34px; border-bottom: 1px solid var(--accent-green); }
</style>
</head>
<body>
<main class="screen">
  <div class="backdrop" role="img" aria-label="Faint photo of an office corridor with doors, tinted red"></div>

  <header class="status-bar">
    <svg class="signal" width="70" height="12" viewBox="0 0 70 12">
      <g fill="#fff"><circle cx="4" cy="5" r="3.5"/><circle cx="13" cy="5" r="3.5"/><circle cx="22" cy="5" r="3.5"/><circle cx="31" cy="5" r="3.5"/><circle cx="40" cy="5" r="3.5"/></g>
      <g fill="none" stroke="#fff" stroke-width="1.6" stroke-linecap="round">
        <path d="M52 4.5a9 9 0 0 1 12 0"/><path d="M54.5 7a5.5 5.5 0 0 1 7 0"/>
      </g>
      <circle cx="58" cy="10" r="1.5" fill="#fff"/>
    </svg>
    <div class="time">9:41 PM</div>
    <div class="power">
      <svg width="8" height="14" viewBox="0 0 8 14"><path d="M1 4l6 6-3 3V1l3 3-6 6" fill="none" stroke="rgba(255,255,255,0.7)" stroke-width="1.2"/></svg>
      <span>100%</span>
      <svg width="30" height="14" viewBox="0 0 30 14"><rect x="0.5" y="0.5" width="26" height="13" rx="2.5" fill="none" stroke="#fff"/><rect x="2.5" y="2.5" width="22" height="9" rx="1" fill="#fff"/><rect x="27.5" y="4.5" width="2" height="5" rx="1" fill="#fff"/></svg>
    </div>
  </header>

  <h1 class="brand-name">Quillstone security</h1>

  <h2 class="page-title"><span>Sign Up</span></h2>

  <div class="field field-email">
    <span class="value">jhonedoie@example.com<span class="caret"></span></span>
    <svg width="36" height="28" viewBox="0 0 36 28"><rect x="0" y="0" width="36" height="28" rx="2" fill="#fff"/><path d="M1 2l17 13L35 2M1 26l12-12M35 26L23 14" fill="none" stroke="#c4505f" stroke-width="2"/></svg>
  </div>

  <div class="field field-password">
    <span class="placeholder">Password</span>
    <svg width="30" height="40" viewBox="0 0 30 40"><path d="M7 17V11a8 8 0 0 1 16 0v6" fill="none" stroke="#fff" stroke-width="4"/><rect x="1" y="16" width="28" height="23" rx="3" fill="#fff"/><circle cx="15" cy="26" r="3" fill="#c4505f"/><rect x="13.5" y="26" width="3" height="7" fill="#c4505f"/></svg>
  </div>

  <div class="field field-confirm">
    <span class="placeholder">Confirm Password</span>
    <svg width="30" height="40" viewBox="0 0 30 40"><path d="M7 17V11a8 8 0 0 1 16 0v6" fill="none" stroke="#fff" stroke-width="4"/><rect x="1" y="16" width="28" height="23" rx="3" fill="#fff"/><circle cx="15" cy="26" r="3" fill="#c4505f"/><rect x="13.5" y="26" width="3" height="7" fill="#c4505f"/></svg>
  </div>

  <label class="touch-option">
    <span class="checkbox"><svg width="22" height="18" viewBox="0 0 22 18"><path d="M2 9l6 6L20 2" fill="none" stroke="var(--accent-green)" stroke-width="2"/></svg></span>
    <span>Enable Touch</span>
  </label>

  <div class="register-button">Register</div>

  <p class="login-prompt">Already have an account? <span class="login-link">LOGIN</span> now</p>
</main>
</body>
</html>
```